Flyer Needed to Advertise New Online Reading Programs

ABOUT THE TRUST OF READING DEVELOPMENT
The Trust teaches summer reading skills programs for elementary school students, in programs offered through partnerships with universities, colleges and municipalities nationwide. The goal of each program is to build reading skills, and to foster a lifetime love of books and reading.

AIMS & TARGET MARKET
The Trust has developed a new format of its’ online reading program for elementary students, which includes live small-group video classes taught by a professional reading teacher. The Trust seeks a new graphic design for a flyer to advertise the new online reading program. The flyer will be sent to elementary schools, passed out by teachers, and then taken home by students to show parents; therefore, the primary audience for the flyer will be teachers and parents of elementary school students.

Live classes for children are completely new in online education, unlike anything else in the marketplace, and parents and teachers therefore have no experience with them. The successful design will include illustrations or photographs that allow visitors to immediately grasp/understand the new video class format, without relying heavily on a written description. Additionally, the successful flyer concept will make the program, and the video classes in particular, feel fun and appealing to kids and parents.

Below is additional information about the new live small-group video class format, which meets weekly for 6 weeks:
o During video classes, students participate from home.
o During discussions, the student’s computer (or tablet) screen is filled with live video frames of the teacher and the other students. The video frame for the teacher is larger, and the other students appear in smaller frames.
o During other video class instruction, the teacher uses a presentation screen to display pages of a book or a “whiteboard” used for instructional activities.

Notes: The flyer design could include an illustrated or photo screenshot of a video class, with children looking engaged and a teacher leading them in discussion (stock photos are okay to use in flyer design). We have included a screen shot of one of these classes for reference, but do not feel constrained to represent this screen realistically (as shown here). Layout, look and feel can be changed. Alternatively, you may choose to use a graphic other than a screenshot to bring across the concept of the video classes.

COPY AND SPECIFICATIONS
The flyer design will be one-sided and the dimensions are 8.5” x 11” in either portrait or landscape orientation. We will consider designs in color or black and white. Since we brand our flyers with logos of the universities we partner with throughout the nation, we’ll need to include a partner logo in the design. Exact copy will be provided, but layout is flexible. Screenshots from our sample classes are included to show screen layout. Stock photos are okay to use in flyer designs.

Reason: We'd like to make edits to existing designs.

Hi designers, We wanted to share our thoughts on the main image of the flyer. We're leaning towards an image that shows a sole student on a computer with the computer screen in view. The computer screen could have the sample image we provided to show how the video classes operate. Thanks! The Trust of Reading Development

Graphic Design

```html
<!DOCTYPE html>
<html lang="en">
<head>
<meta charset="utf-8">
<title>Reading Skills Classes Flyer</title>
<link href="https://fonts.googleapis.com/css2?family=Lato:ital,wght@0,300;0,400;0,700;0,900;1,700&family=Oswald:wght@500&display=swap" rel="stylesheet">
<style>
  :root {
    --page-bg: #e9e9ea;
    --cyan: #16bcd9;
    --panel-dark: #232323;
    --white: #ffffff;
    --ink: #2a2a2a;
    --body-ink: #3d3d3d;
    --rule: #5a5a5a;
    --photo-a: #dfe7ea;
    --photo-b: #c9a98e;
  }
  * { box-sizing: border-box; margin: 0; padding: 0; }
  html, body { width: 800px; height: 1200px; overflow: hidden; }
  body {
    background: var(--page-bg);
    font-family: "Lato", Arial, sans-serif;
    position: relative;
  }
  .flyer {
    position: absolute;
    left: 36px; top: 95px;
    width: 729px; height: 935px;
    background: var(--white);
    box-shadow: 0 6px 14px rgba(0,0,0,0.28);
    overflow: hidden;
  }
  .hero-band {
    position: absolute; left: 0; top: 0;
    width: 263px; height: 313px;
    background: var(--cyan);
    color: var(--white);
  }
  .partner-mark {
    position: absolute; left: 52px; top: 10px;
    width: 164px; height: 72px;
    background: var(--panel-dark);
    display: flex; flex-direction: column; align-items: center; justify-content: center;
    font-weight: 400; font-size: 21px; line-height: 1.1; letter-spacing: 1px;
    color: var(--white);
  }
  .partner-mark .small { font-size: 17px; letter-spacing: 1.5px; }
  .hero-title {
    position: absolute; left: 17px; top: 86px;
    font-weight: 700; font-size: 57px; line-height: 66px;
  }
  .hero-sub {
    position: absolute; left: 17px; top: 217px;
    font-weight: 300; font-size: 44px;
  }
  .hero-tag {
    position: absolute; left: 23px; top: 272px;
    font-weight: 400; font-size: 22px;
  }
  .hero-photo {
    position: absolute; left: 263px; top: 0;
    width: 466px; height: 313px;
    background: linear-gradient(120deg, var(--photo-a) 0%, #e8d8c8 45%, var(--photo-b) 75%, #e3a06a 100%);
  }
  .side-panel {
    position: absolute; left: 0; top: 313px;
    width: 263px; height: 622px;
    background: var(--panel-dark);
    color: var(--white);
  }
  .feature {
    position: absolute; left: 19px;
    display: flex; align-items: center; gap: 8px;
    font-size: 13px; line-height: 16px;
  }
  .feature svg { flex: none; }
  .side-rule {
    position: absolute; left: 12px; width: 232px; height: 1px;
    background: var(--rule);
  }
  .skills-heading {
    position: absolute; left: 28px; top: 250px;
    font-size: 16px; font-weight: 700; letter-spacing: 1.5px;
  }
  .skills-list {
    position: absolute; left: 28px; top: 275px;
    list-style: none; font-size: 15px; font-weight: 400; line-height: 20px;
  }
  .skills-list li { height: 28.5px; }
  .contact {
    position: absolute; left: 28px; top: 470px;
  }
  .contact-heading { font-size: 18px; font-weight: 700; line-height: 23px; }
  .contact-phone { font-size: 18px; font-weight: 700; font-style: italic; line-height: 22px; }
  .hours { margin-top: 6px; font-size: 13px; line-height: 16px; }
  .hours b { font-weight: 700; }
  .programs {
    position: absolute; left: 281px; top: 332px; width: 430px;
    color: var(--body-ink);
  }
  .programs-heading {
    font-size: 16px; font-weight: 700; letter-spacing: 1.2px; color: var(--ink);
    margin-bottom: 9px;
  }
  .program { position: absolute; left: 0; width: 430px; }
  .program h3 { font-size: 12.5px; font-weight: 700; color: var(--ink); line-height: 15px; }
  .program p { font-size: 10.5px; line-height: 13.4px; }
  .partners {
    position: absolute; left: 297px; top: 888px;
    display: flex; align-items: center; gap: 25px;
    color: var(--ink);
  }
  .partners .label { font-size: 15px; font-weight: 900; letter-spacing: 0.2px; }
  .partners .slot { font-family: "Oswald", Arial, sans-serif; font-size: 17px; font-weight: 500; }
</style>
</head>
<body>
<main class="flyer">
  <section class="hero-band">
    <div class="partner-mark"><span>EASTBROOK</span><span class="small">UNIVERSITY</span></div>
    <h1 class="hero-title">Reading<br>Skills</h1>
    <div class="hero-sub">Classes</div>
    <div class="hero-tag">Online this Summer!</div>
  </section>
  <div class="hero-photo" role="img" aria-label="Photo of a smiling teacher helping a group of young children read at a classroom table"></div>

  <aside class="side-panel">
    <div class="feature" style="top:32px">
      <svg width="34" height="34" viewBox="0 0 34 34"><circle cx="17" cy="17" r="17" fill="var(--cyan)"/><rect x="8" y="10" width="18" height="12" rx="1" fill="none" stroke="#fff" stroke-width="1.8"/><rect x="13" y="24" width="8" height="1.8" fill="#fff"/></svg>
      <span>Small class size</span>
    </div>
    <div class="feature" style="top:76px">
      <svg width="34" height="34" viewBox="0 0 34 34"><circle cx="17" cy="17" r="17" fill="var(--cyan)"/><circle cx="17" cy="10" r="3" fill="#fff"/><path d="M12 18c0-3 2-4.5 5-4.5s5 1.5 5 4.5z" fill="#fff"/><rect x="11" y="19" width="12" height="8" fill="#fff"/></svg>
      <span>A skilled and encouraging teacher</span>
    </div>
    <div class="feature" style="top:119px">
      <svg width="34" height="34" viewBox="0 0 34 34"><circle cx="17" cy="17" r="17" fill="var(--cyan)"/><circle cx="17" cy="12.5" r="4.5" fill="#fff"/><path d="M9 26c0-5 3.5-8 8-8s8 3 8 8z" fill="#fff"/></svg>
      <span>Individualized skills intruction</span>
    </div>
    <div class="feature" style="top:166px">
      <svg width="34" height="34" viewBox="0 0 34 34"><circle cx="17" cy="17" r="17" fill="var(--cyan)"/><rect x="11" y="8" width="12" height="17" rx="1" fill="#fff"/><rect x="11" y="23" width="12" height="3" fill="var(--cyan)" stroke="#fff" stroke-width="1"/></svg>
      <span>A program of independent<br>reading in great books</span>
    </div>

    <div class="side-rule" style="top:228px"></div>
    <h2 class="skills-heading">READING SKILLS:</h2>
    <ol class="skills-list">
      <li>1. Phonics</li>
      <li>2. Comprehension</li>
      <li>3. Fluency</li>
      <li>4. Study Skills</li>
      <li>5.Speed Reading</li>
      <li>6.Love of Reading</li>
    </ol>
    <div class="side-rule" style="top:459px"></div>

    <div class="contact">
      <div class="contact-heading">For More Information or<br>to Register</div>
      <div class="contact-phone">Call 1-800-555-0142</div>
      <div class="hours">
        <div><b>Mon.-Fri :</b> 5am - 7pm</div>
        <div><b>Sat :</b> 5am - 4pm</div>
        <div><b>Sun :</b> 6am- 4pm</div>
      </div>
    </div>
  </aside>

  <section class="programs">
    <h2 class="programs-heading">PROGRAM DESCRIPTIONS:</h2>
    <div class="program" style="top:30px">
      <h3>Program for Preschoolers:</h3>
      <p>Students in this program build strong reading readiness skills.<br>Your child will learn letter recognition and beginning phonics,<br>and develop the motivation and love of reading that make learning to read easy, enjoy-<br>able, and successful.</p>
    </div>
    <div class="program" style="top:106px">
      <h3>Program for Kindergartners:</h3>
      <p>Students in this program learn beginning reading skills and develop a love of books.<br>Your child will learn letter recognition, phonics, and sight words, and will learn to sound<br>out short words.</p>
    </div>
    <div class="program" style="top:171px">
      <h3>Program for Entering 1st Graders:</h3>
      <p>Students in this program learn to read independently. Your child will learn phonics and<br>sight words, build comprehension, and gain the skills and confidence needed for suc-<br>cess in first grade.</p>
    </div>
    <div class="program" style="top:235px">
      <h3>Program for Entering 2nd Graders:</h3>
      <p>Students in this program become fluent, independent readers. Your child will make sig-<br>nificant gains in phonics and word-attack skills, fluency, and comprehension, and will de-<br>velop confidence and a love of reading.</p>
    </div>
    <div class="program" style="top:298px">
      <h3>Program for Entering 3rd Graders:</h3>
      <p>Students in this program become strong independent readers. Your child will develop the<br>comprehension, fluency, and long-word decoding skills needed to read longer books with<br>ease, and will build confidence and a love of reading.</p>
    </div>
    <div class="program" style="top:371px">
      <h3>Program for Entering 4th and 5th Graders:</h3>
      <p>Students in this program make substantial gains in comprehension, long-word decoding<br>skills, fluency, and reading speed. Your child will complete homework more quickly and<br>easily, be more successful in school, and become a strong, enthusiastic reader.</p>
    </div>
    <div class="program" style="top:439px">
      <h3>Programs for Entering 6th-8th Graders and Entering 9th and 10th Graders:</h3>
      <p>Students in these programs make substantial gains in comprehension while doubling<br>reading speed. They also learn the best way to read textbooks, take notes, and study for<br>tests. As a result, students complete homework more quickly and easily, get better grades,<br>and enjoy reading more.</p>
    </div>
  </section>

  <footer class="partners">
    <span class="label">OUR PARTNER</span>
    <span class="slot">LOGO1</span>
    <span class="slot">LOGO2</span>
    <span class="slot">LOGO2</span>
  </footer>
</main>
</body>
</html>
```